Nutrition Supplements needs Logo and Package Design

We need logo and label design for the new nutrition and dietary supplement brand called "Fern Ledger".
It is a new brand for western world but is based on 150 year old formulations successfully sold in the East.

The first five formulations are slated to be launched in the US in November.
They will aid in conditions like:
1. Product One: Diabetes,
2. Product Two: Heart Health,
3. Product Three: Men's Health & Vitality,
4. Product Four: Women's Health and Menstrual conditions,
5. Product Five: Sport Nutrition Aid in keeping mind and body agile.

The competition will be Brightmeadow own brands and brands like Kelpstone Path.

All the five products will be packaged in HDPE bottle ( 1 bottle has 60 capsules )
Height / length : 94.5 mm
Width : 51 mm

Please feel free to ask any additional questions.

Reason: We are new to this website and modes of operation. We have added participation budget to the project from today. We are also launching a project on pixel harbor for website design tomorrow. This website will be for the same products for which this packaging design project is launched. We are excited to find good designers on this platform that we can work with in the long term

Target Market(s)

Females in the age group 30 - 75.
Aware of nutrition supplements and their benefits, the label will have to stand out when it's next to brands like Brightmeadow, Kelpstone path etc.. in the nutrition isle.
shop at stores like RVT, Brightmeadow, Internet, Merchant Olly's, Pantry Lane.

Industry/Entity Type

Nutrition

Requirements
Nice to have
• It would be nice to have logo design that vibrates combination of freshness, power of traditional remedies, age old secrets, and age defiance.

```html
<!DOCTYPE html>
<html lang="en">
<head>
<meta charset="utf-8">
<title>Fern Ledger – Supplement Labels</title>
<link rel="stylesheet" href="https://fonts.googleapis.com/css2?family=Cormorant+SC:wght@500&family=Princess+Sofia&display=swap">
<style>
  :root {
    --canvas: #ffffff;
    --ink: #8a7a55;
    --card: #ffffff;
    --rule: #9a8c68;
    --mint: #a8d8c3;
    --mint-tint: #c7e6d8;
    --coral: #f48a85;
    --coral-tint: #f8c4c1;
    --slate: #6b7b85;
    --slate-tint: #bcc7cd;
    --lime: #c4dc7c;
    --lime-tint: #dbeaa9;
    --lavender: #9b99cb;
    --lavender-tint: #c9c7e4;
  }
  * { margin: 0; padding: 0; box-sizing: border-box; }
  html, body {
    width: 1200px; height: 378px; overflow: hidden;
    background: var(--canvas);
  }
  .label-range {
    position: relative; width: 1200px; height: 378px;
  }
  .label {
    position: absolute; top: 0; width: 203px; height: 378px;
    background: var(--band);
  }
  .label--diabetes { left: 60px;  --band: var(--mint);     --tint: var(--mint-tint); }
  .label--heart    { left: 285px; --band: var(--coral);    --tint: var(--coral-tint); }
  .label--men      { left: 510px; --band: var(--slate);    --tint: var(--slate-tint); }
  .label--women    { left: 735px; --band: var(--lime);     --tint: var(--lime-tint); }
  .label--sport    { left: 962px; --band: var(--lavender); --tint: var(--lavender-tint); }

  .brand-card {
    position: absolute; left: 28px; top: 40px; width: 148px; height: 172px;
    background: var(--card); border-radius: 18px;
    display: flex; flex-direction: column; align-items: center; justify-content: center;
    gap: 14px;
  }
  .brand-dot {
    width: 34px; height: 34px; border-radius: 50%;
    background: var(--band);
  }
  .brand-name {
    font-family: "Cormorant SC", serif; font-weight: 500;
    font-size: 21px; letter-spacing: 0.3px; color: var(--ink);
    white-space: nowrap;
  }

  .condition-panel {
    position: absolute; left: 6px; top: 277px; width: 191px; height: 101px;
    background: var(--tint);
  }
  .condition-panel .rule {
    position: absolute; left: 20px; right: 20px; height: 0;
    border-top: 1px dotted var(--rule);
  }
  .rule--1 { top: 42px; }
  .rule--2 { top: 58px; }
  .rule--3 { top: 74px; }
  .condition {
    position: absolute; left: 0; right: 0; top: 24px;
    text-align: center; white-space: nowrap;
    font-family: "Princess Sofia", cursive;
    color: var(--ink); font-size: 14px; line-height: 16.5px;
  }
  .condition--single { font-size: 18px; line-height: 22px; top: 14px; }
</style>
</head>
<body>
<main class="label-range">

  <section class="label label--diabetes">
    <div class="brand-card"><span class="brand-dot"></span><span class="brand-name">Fern Ledger</span></div>
    <div class="condition-panel">
      <span class="rule rule--1"></span><span class="rule rule--2"></span><span class="rule rule--3"></span>
      <p class="condition condition--single">Diabetes</p>
    </div>
  </section>

  <section class="label label--heart">
    <div class="brand-card"><span class="brand-dot"></span><span class="brand-name">Fern Ledger</span></div>
    <div class="condition-panel">
      <span class="rule rule--1"></span><span class="rule rule--2"></span><span class="rule rule--3"></span>
      <p class="condition condition--single">Heart's Health</p>
    </div>
  </section>

  <section class="label label--men">
    <div class="brand-card"><span class="brand-dot"></span><span class="brand-name">Fern Ledger</span></div>
    <div class="condition-panel">
      <span class="rule rule--1"></span><span class="rule rule--2"></span><span class="rule rule--3"></span>
      <p class="condition">Men's Health<br>&amp;<br>Vitality</p>
    </div>
  </section>

  <section class="label label--women">
    <div class="brand-card"><span class="brand-dot"></span><span class="brand-name">Fern Ledger</span></div>
    <div class="condition-panel">
      <span class="rule rule--1"></span><span class="rule rule--2"></span><span class="rule rule--3"></span>
      <p class="condition">Women's Health<br>&amp;<br>Menstrual conditions</p>
    </div>
  </section>

  <section class="label label--sport">
    <div class="brand-card"><span class="brand-dot"></span><span class="brand-name">Fern Ledger</span></div>
    <div class="condition-panel">
      <span class="rule rule--1"></span><span class="rule rule--2"></span><span class="rule rule--3"></span>
      <p class="condition">Sport Nutrition Aid<br>in keeping<br>mind and body agile</p>
    </div>
  </section>

</main>
</body>
</html>
```